Business Card Design Project

See the detainl of the Vortel company project I also have live: http://tasks.quillmarsh.com/task.aspx?id=382917

Reason: I am waiting to select a logo design and ideally the business card design will be from the same person

Industry/Entity Type

Business

```html
<!DOCTYPE html>
<html lang="en">
<head>
<meta charset="utf-8">
<title>Vortel Business Card</title>
<link href="https://fonts.googleapis.com/css2?family=Roboto:wght@300;400&display=swap" rel="stylesheet">
<style>
  :root {
    --red: #e0473f;
    --charcoal: #333334;
    --charcoal-light: #3b3b3c;
    --ink-light: #f2f2f2;
    --rule: rgba(255,255,255,0.35);
    --backdrop: #e8e8e8;
  }
  * { margin: 0; padding: 0; box-sizing: border-box; }
  html, body {
    width: 1200px; height: 834px; overflow: hidden;
    background: var(--backdrop);
    font-family: "Roboto", Arial, sans-serif;
    font-weight: 300;
    color: var(--ink-light);
  }
  .stage { position: relative; width: 1200px; height: 834px; }
  .card {
    position: absolute; top: 267px;
    width: 520px; height: 300px;
    overflow: hidden;
    box-shadow: 0 8px 24px rgba(0,0,0,0.18);
  }
  .card-back { left: 50px; background: var(--red); }
  .card-front { left: 630px; background: var(--charcoal); }
  .card-shapes { position: absolute; inset: 0; }

  .brand { display: flex; align-items: center; gap: 8px; }
  .brand-dot { width: 14px; height: 14px; border-radius: 50%; background: var(--ink-light); }
  .brand-name { font-size: 13px; font-weight: 400; letter-spacing: 1px; }

  .back-identity {
    position: absolute; left: 0; right: 0; top: 108px;
    display: flex; flex-direction: column; align-items: center; gap: 10px;
  }
  .web-address {
    font-size: 15px; font-style: italic; letter-spacing: 0.3px;
    padding: 0 6px 6px; border-bottom: 1px dashed var(--rule);
  }

  .front-identity { position: absolute; left: 40px; top: 46px; }
  .person-name {
    margin-top: 14px; font-size: 17px; letter-spacing: 1.6px;
  }
  .person-role {
    display: inline-block; margin-top: 6px; padding-bottom: 6px;
    font-size: 12px; letter-spacing: 0.5px;
    border-bottom: 1px dashed var(--rule);
  }

  .contact-list {
    position: absolute; left: 150px; top: 158px; width: 330px;
    list-style: none;
  }
  .contact-item {
    display: flex; align-items: flex-start; gap: 12px;
    padding: 8px 0 7px; font-size: 13.5px; line-height: 1.35;
    border-bottom: 1px solid var(--rule);
  }
  .contact-icon { width: 14px; height: 14px; flex: none; margin-top: 2px; fill: var(--ink-light); }
</style>
</head>
<body>
<main class="stage">

  <section class="card card-back" aria-label="Card back">
    <svg class="card-shapes" viewBox="0 0 520 300" aria-hidden="true">
      <polygon points="280,300 520,228 520,300" fill="var(--charcoal)"/>
    </svg>
    <div class="back-identity">
      <div class="brand">
        <span class="brand-dot"></span>
        <span class="brand-name">Vortel</span>
      </div>
      <p class="web-address">www.VortelStudio.com</p>
    </div>
  </section>

  <section class="card card-front" aria-label="Card front">
    <svg class="card-shapes" viewBox="0 0 520 300" aria-hidden="true">
      <polygon points="0,0 520,0 520,8 0,52" fill="var(--red)"/>
      <polygon points="400,175 520,150 520,300 418,300" fill="var(--charcoal-light)"/>
      <line x1="400" y1="175" x2="418" y2="300" stroke="var(--red)" stroke-width="2.5"/>
    </svg>

    <div class="front-identity">
      <div class="brand">
        <span class="brand-dot"></span>
        <span class="brand-name">Vortel</span>
      </div>
      <h1 class="person-name">NORA K.VELSIN</h1>
      <p class="person-role">Creative Director</p>
    </div>

    <ul class="contact-list">
      <li class="contact-item">
        <svg class="contact-icon" viewBox="0 0 24 24" aria-hidden="true"><path d="M6.6 10.8a15.1 15.1 0 0 0 6.6 6.6l2.2-2.2a1 1 0 0 1 1-.25 11.4 11.4 0 0 0 3.6.57 1 1 0 0 1 1 1V20a1 1 0 0 1-1 1A17 17 0 0 1 3 4a1 1 0 0 1 1-1h3.5a1 1 0 0 1 1 1c0 1.25.2 2.45.57 3.6a1 1 0 0 1-.25 1z"/></svg>
        <span>+10 432 718 6</span>
      </li>
      <li class="contact-item">
        <svg class="contact-icon" viewBox="0 0 24 24" aria-hidden="true"><path d="M2 5h20v14H2zm2 2v.5l8 5 8-5V7zm0 2.9V17h16V9.9l-8 5z"/></svg>
        <span>nvelsin@vortelmail.com</span>
      </li>
      <li class="contact-item">
        <svg class="contact-icon" viewBox="0 0 24 24" aria-hidden="true"><path d="M12 3 2 12h3v9h5v-6h4v6h5v-9h3z"/></svg>
        <span>48 harrowgate rd, linden vale, Ohara,USA</span>
      </li>
    </ul>
  </section>

</main>
</body>
</html>
```